Webdesign für Blog zum Thema KINDERWUNSCH
Zielgruppe
Hallo, ich bin 41 Jahre alt und lebe mit meinem Mann und unseren beiden Kindern (und Hund Ki;)) in einem kleinen Ort im Rhein-Main-Gebiet.
Ich musste auf meine beiden Kinder jeweils lange warten und diese schwere Zeit habe ich nicht vergessen. Meine beste Freundin hat mich irgendwann dazu überredet, anderen Frauen, denen es ähnlich geht, zu helfen. Besonders kann ich mich daran erinnern, wie schwer es war, verlässliche, gut recherchierte Quellen zum Thema Kinderwunsch zu finden.
Zusammen mit meiner besten Freundin baue ich daher einen Blog auf, bei dem es genau um diese Themen gehen soll.
Zielgruppe:
• Frauen
• Mitte / Ende 30
• Verheiratet, keine Kinder
• Höheres Bildungsniveau / nicht zwingend Akademiker
Kernemotionen:
o grübelt / ist unsicher
o nimmt ungewollte Kinderlosigkeit persönlich
o ängstlich / teils verzweifelt
o ungeduldig
Aufgabenstellung
Es geht um das Design unseres Blogs.
Uns ist besonders wichtig, dass der Blog das Spannungsverhältnis Seriosität – Freude – Ruhe vermittelt.
Das Design soll folgendes transportieren:
• Seriös / glaubwürdig
• Hochwertig
• Sicherheit / Ruhe / Seelenfriede
• Hoffnung
• Positiv / herzlich / unbeschwert – aber dennoch ernsthaft
ZUM FARBKONZEPT ETC. SIEHE BITTE BRIEFING ANBEI

```html
<!DOCTYPE html>
<html lang="de">
<head>
<meta charset="utf-8">
<title>Carolin Weber – Webdesign für Blog zum Thema Kinderwunsch</title>
<link rel="stylesheet" href="https://fonts.googleapis.com/css2?family=Josefin+Sans:wght@300;400&family=Open+Sans:wght@400;600;700&display=swap">
<style>
:root{
  --board:#ececec;
  --blue:#6a93b5;
  --blue-dark:#5b85a9;
  --tint:#eaf1f9;
  --tint-2:#dde8f4;
  --ink:#2e2e2e;
  --text:#6d6d6d;
  --muted:#9a9a9a;
  --white:#ffffff;
}
*{box-sizing:border-box;margin:0;padding:0}
html,body{width:1200px;height:2400px;overflow:hidden;background:var(--board)}
body{font-family:"Open Sans",Arial,sans-serif;color:var(--text)}
.canvas{position:relative;width:1200px;height:2400px;overflow:hidden}
.board{position:absolute;left:0;top:0;width:1288px;height:2576px;overflow:hidden;transform:scale(.93168);transform-origin:0 0;background:linear-gradient(180deg,#efefef,#e9e9e9)}

.board-title{position:absolute;left:58px;top:70px;width:1190px;font-family:"Josefin Sans",sans-serif;font-weight:300;font-size:80px;letter-spacing:.38em;color:var(--blue);white-space:nowrap;line-height:1;overflow:hidden}
.board-subtitle{position:absolute;right:46px;top:172px;font-family:"Josefin Sans",sans-serif;font-weight:400;font-size:22px;letter-spacing:.32em;color:var(--blue);white-space:nowrap}
.hero-photo{position:absolute;left:610px;top:250px;width:678px;height:440px;background:radial-gradient(ellipse at 40% 35%,#f1dccd 0,#ead2c2 18%,#f3f3f3 40%,transparent 62%),radial-gradient(ellipse at 78% 70%,#b9d0ea 0,#cfdff0 25%,transparent 55%),linear-gradient(180deg,#f4f4f4,#ececec)}

.caption{position:absolute;font-family:"Josefin Sans",sans-serif;font-weight:300;font-size:22px;letter-spacing:.08em;color:var(--ink)}

.page{position:absolute;width:556px;background:var(--white);box-shadow:0 2px 8px rgba(0,0,0,.08);overflow:hidden}
.site-header{height:98px;text-align:center;padding-top:27px}
.site-name{font-family:"Josefin Sans",sans-serif;font-weight:300;font-size:25px;letter-spacing:.36em;color:var(--ink);margin-right:-.36em}
.site-slogan{font-family:"Josefin Sans",sans-serif;font-weight:300;font-size:13.5px;letter-spacing:.06em;color:var(--ink);margin-top:2px}
.site-nav{height:26px;background:var(--tint);display:flex;justify-content:center;align-items:center;gap:26px;font-size:6px;letter-spacing:.05em;text-transform:uppercase;color:var(--ink)}
.site-nav .active{color:var(--blue)}
.site-nav .active::before{content:"› ";font-weight:700}

.site-body{position:relative;padding:38px 45px 0}
.main{width:318px}
.post-title{font-family:"Open Sans",sans-serif;font-weight:400;font-size:12.5px;line-height:16px;color:var(--ink)}
.post-meta{font-size:5.5px;color:var(--muted);margin:6px 0 8px;display:flex;gap:10px}
.post-meta span::before{content:"";display:inline-block;width:4px;height:4px;background:var(--muted);margin-right:4px;vertical-align:-.5px}
.post-image{width:317px;height:123px;border:1px solid #ececec;margin-bottom:16px}
.img-sleeping{background:radial-gradient(ellipse at 55% 55%,#f2f0ec 0,#e9e4dc 22%,transparent 45%),radial-gradient(ellipse at 35% 65%,#edd8c8 0,transparent 30%),linear-gradient(180deg,#f4f4f4,#dcdcdc)}
.img-crawling{background:radial-gradient(ellipse at 58% 40%,#f0d6c4 0,#e7c6b0 14%,transparent 30%),radial-gradient(ellipse at 55% 85%,#3a84d0 0,#5d9ee0 18%,transparent 40%),linear-gradient(180deg,#d8e7f6,#f4f7fb 60%,#e8eef5)}
.post-text{font-size:6.6px;line-height:12px;color:var(--text)}
.post-text p+p{margin-top:12px}
.read-more{display:inline-block;font-size:6.4px;font-weight:700;color:var(--blue);text-transform:uppercase;margin:14px 0 36px}
.read-more::after{content:" ›";font-size:9px}

.sidebar{position:absolute;top:40px;right:34px;width:131px;border:6px solid var(--tint);text-align:center;padding:16px 10px 0}
.avatar{width:96px;height:96px;border-radius:50%;margin:0 auto 24px;background:radial-gradient(circle at 50% 40%,#efd0b5 0,#e0b48f 22%,#c9a268 40%,#9dbb7a 70%,#7ea564 100%)}
.side-heading{font-size:6px;font-weight:700;letter-spacing:.08em;text-transform:uppercase;color:var(--ink);margin-bottom:12px}
.side-text{font-size:5.6px;line-height:9.4px;color:var(--text);padding-bottom:16px;border-bottom:1px solid var(--tint);margin-bottom:16px}
.social{display:flex;justify-content:center;gap:10px;padding-bottom:16px;border-bottom:1px solid var(--tint);margin-bottom:16px}
.social span{width:9px;height:9px;border-radius:50%;background:var(--blue)}
.topic-list{list-style:none;text-align:left;padding-left:8px;font-size:5.6px;line-height:11px;color:var(--blue)}
.topic-list li::before,.link-list li::before{content:"+";font-weight:700;margin-right:5px;color:var(--blue)}

.site-footer{position:absolute;left:0;bottom:20px;width:100%;height:118px;background:var(--tint);padding:22px 45px 0;display:flex;gap:18px}
.footer-col h4{font-size:5.6px;font-weight:700;text-transform:uppercase;color:var(--blue);margin-bottom:10px;letter-spacing:.03em}
.footer-about{width:140px}
.footer-about .row{display:flex;gap:7px}
.footer-about .avatar{width:44px;height:44px;margin:0;flex:none}
.footer-about p,.footer-col ul{font-size:5.2px;line-height:9px;color:var(--blue)}
.footer-col ul{list-style:none}
.footer-follow{width:62px}
.footer-follow .social{justify-content:flex-start;border:0;padding:0;gap:8px}
.footer-links{width:60px}
.link-cols{display:flex;gap:22px}
.site-copy{position:absolute;left:0;bottom:0;width:100%;height:20px;background:var(--blue);color:var(--white);font-size:5px;text-align:center;line-height:20px}

.about-title{text-align:center;font-size:12.5px;color:var(--ink);font-weight:400;margin-bottom:28px}
.about-text{width:280px;font-size:6.6px;line-height:12px}
.about-text .lead{font-weight:700;color:#4b4b4b;margin-bottom:12px}
.about-photo{position:absolute;right:0;top:70px;width:226px;height:193px;background:radial-gradient(ellipse at 45% 45%,#eccab0 0,#d9a987 20%,transparent 40%),radial-gradient(ellipse at 60% 90%,#c9a37c 0,transparent 40%),linear-gradient(90deg,#ffffff 0,#e5ecd6 30%,#9fbf7f 70%,#7aa35e)}

.article-title{font-size:12.5px;line-height:16px;color:var(--ink);font-weight:400}
.article h3{font-size:10.8px;font-weight:700;color:var(--blue);margin:20px 0 7px}
.article p{font-size:6.6px;line-height:12px}
.article p+p{margin-top:12px}
.article .quote{font-style:italic;font-weight:700;color:#4e4e4e}
.article strong{color:#4b4b4b}
.info-box{position:relative;background:var(--tint-2);padding:10px 70px 10px 10px;margin-top:14px;height:90px}
.info-box h5{font-size:6.6px;font-weight:700;color:var(--blue)}
.info-box p{color:var(--blue)}
.info-box svg{position:absolute;right:6px;top:4px}
.pager{display:flex;justify-content:space-between;margin-top:30px;font-size:6.4px;font-weight:700;color:var(--blue);text-transform:uppercase}
</style>
</head>
<body>
<div class="canvas">
<div class="board">
  <div class="board-title">CAROLIN WEBER</div>
  <div class="board-subtitle">WEBDESIGN FÜR BLOG ZUM THEMA KINDERWUNSCH</div>
  <div class="hero-photo" role="img" aria-label="Foto: lachendes Baby in blau-weiß gestreiftem Strampler auf hellem Hintergrund"></div>

  <section class="page" style="left:60px;top:395px;height:986px">
    <header class="site-header"><div class="site-name">CAROLIN WEBER</div><div class="site-slogan">Slogan - Subheadline</div></header>
    <nav class="site-nav"><span class="active">Home</span><span>Blog</span><span>Über mich</span><span>Kontakt</span></nav>
    <div class="site-body">
      <div class="main">
        <article>
          <h2 class="post-title">Wie bekomme ich sofort einen Termin beim Frauenarzt?</h2>
          <div class="post-meta"><span>03. Oktober 2017</span><span>2 Kommentare</span><span>Blogthema</span></div>
          <div class="post-image img-sleeping" role="img" aria-label="Foto: schlafendes Neugeborenes auf weißer Decke"></div>
          <div class="post-text"><p>"Tut mir leid, die nächsten drei Monate sind wir voll ausgebucht!" - Worte, die jedem Patienten Ohrenschmerzen bereiten. Bei einem Facharzt sind sie bereits zum Standardrepertoire geworden, beim Gynäkologen. Wer hier auf einen schnellen Termin hofft, wartet oft vergebens. Nicht selten beträgt die Wartezeit bis zu vier Monate. Dem einen mögen vier Monate vielleicht wie nichts erscheinen, Frauen wie mir hingegen wie eine Ewigkeit. Wer sich nach neuem Leben sehnt, hat keine Zeit zu warten. So ist jeder verstrichene Tag ein verlorener Tag. Auch du willst dich nicht länger vertrösten lassen? Ich verrate dir meine Tipps, schneller an einen Termin beim Frauenarzt zu kommen.</p></div>
          <span class="read-more">Weiterlesen</span>
        </article>
        <article>
          <h2 class="post-title">Lorem ipsum dolor sit amet, consetetur sadi pscing dolor sit amet consetetur elitr</h2>
          <div class="post-meta"><span>03. Oktober 2017</span><span>2 Kommentare</span><span>Blogthema</span></div>
          <div class="post-image img-crawling" role="img" aria-label="Foto: lachendes Baby in blauem Shirt auf dem Bauch liegend"></div>
          <div class="post-text"><p>Lorem ipsum dolor sit amet, consetetur sadipscing elitr, sed diam nonumy eirmod tempor invidunt ut labore et dolore magna aliquyam erat, sed diam voluptua. At vero eos et accusam et justo duo dolores et ea rebum. Stet clita kasd gubergren, no sea takimata sanctus est Lorem ipsum dolor sit amet. Lorem ipsum dolor sit amet, consetetur sadipscing elitr, sed diam nonumy eirmod tempor invidunt ut labore et dolore magna aliquyam erat, sed diam voluptua. At vero eos et accusam et justo duo dolores et ea rebum. Stet clita kasd gubergren, no sea takimata sanctus est Lorem ipsum dolor sit amet.</p></div>
          <span class="read-more">Weiterlesen</span>
        </article>
      </div>
      <aside class="sidebar" style="height:482px">
        <div class="avatar" role="img" aria-label="Porträtfoto der Bloggerin"></div>
        <div class="side-heading">Herzlich Willkommen</div>
        <div class="side-text">Lorem ipsum dolor sit amet, consetetur sadipscing elitr, sed diam nonumy eirmod tempor invidunt ut labore et dolore magna</div>
        <div class="side-heading">Social Media</div>
        <div class="social"><span></span><span></span><span></span></div>
        <div class="side-heading">Blog Themen</div>
        <ul class="topic-list"><li>Blog-Thema Nummer 1</li><li>Blog-Thema Nummer 2</li><li>Blog-Thema Nummer 3</li><li>Blog-Thema Nummer 4</li><li>Blog-Thema Nummer 5</li><li>Blog-Thema Nummer 6</li></ul>
      </aside>
    </div>
    <footer class="site-footer">
      <div class="footer-col footer-about"><h4>Über Carolin Weber</h4><div class="row"><div class="avatar" role="img" aria-label="Porträtfoto der Bloggerin"></div><p>Lorem ipsum dolor sit amet, consetetur sadipscing elitr, sed diam nonumy eirmod tempor invidunt ut labore et dolore magna aliquyam erat.</p></div></div>
      <div class="footer-col footer-follow"><h4>Folgen Sie mir</h4><div class="social"><span></span><span></span><span></span></div></div>
      <div class="footer-col footer-links"><h4>Wichtige Links</h4><ul><li>Kontakt</li><li>Impressum</li><li>Datenschutz</li></ul></div>
      <div class="footer-col"><h4>Meistgelesene Blogartikel</h4><div class="link-cols"><ul class="link-list"><li>Blogartikel 1</li><li>Blogartikel 2</li><li>Blogartikel 3</li><li>Blogartikel 4</li></ul><ul class="link-list"><li>Blogartikel 5</li><li>Blogartikel 6</li><li>Blogartikel 7</li><li>Blogartikel 8</li></ul></div></div>
    </footer>
    <div class="site-copy">Copyright © 2017 Carolin Weber · info@carolinweber.de | Impressum • Datenschutz | Kontakt</div>
  </section>
  <div class="caption" style="left:60px;top:1393px">Entwurf - Home</div>

  <section class="page" style="left:60px;top:1475px;height:520px">
    <header class="site-header"><div class="site-name">CAROLIN WEBER</div><div class="site-slogan">Slogan - Subheadline</div></header>
    <nav class="site-nav"><span>Home</span><span>Blog</span><span class="active">Über mich</span><span>Kontakt</span></nav>
    <div class="site-body" style="padding-top:38px">
      <h2 class="about-title">At vero eos et accusam et justo duo</h2>
      <div class="about-text">
        <p class="lead">Lorem ipsum dolor sit amet, consetetur sadipscing elitr, sed diam nonumy eirmod tempor invidunt ut labore et dolore magna aliquyam erat, sed diam voluptua.</p>
        <p>At vero eos et accusam et justo duo dolores et ea rebum. Stet clita kasd gubergren, no sea takimata sanctus est Lorem ipsum dolor sit amet. Lorem ipsum dolor sit amet, consetetur sadipscing elitr, sed diam nonumy eirmod tempor invidunt ut labore et dolore magna aliquyam erat, sed diam voluptua. At vero eos et accusam et justo duo dolores et ea rebum.</p>
        <span class="read-more" style="margin-top:14px">Schreiben Sie mir</span>
      </div>
      <div class="about-photo" role="img" aria-label="Porträtfoto der Bloggerin vor grünem Hintergrund"></div>
    </div>
    <footer class="site-footer">
      <div class="footer-col footer-about"><h4>Über Carolin Weber</h4><div class="row"><div class="avatar" role="img" aria-label="Porträtfoto der Bloggerin"></div><p>Lorem ipsum dolor sit amet, consetetur sadipscing elitr, sed diam nonumy eirmod tempor invidunt ut labore et dolore magna aliquyam erat.</p></div></div>
      <div class="footer-col footer-follow"><h4>Folgen Sie mir</h4><div class="social"><span></span><span></span><span></span></div></div>
      <div class="footer-col footer-links"><h4>Wichtige Links</h4><ul><li>Kontakt</li><li>Impressum</li><li>Datenschutz</li></ul></div>
      <div class="footer-col"><h4>Meistgelesene Blogartikel</h4><div class="link-cols"><ul class="link-list"><li>Blogartikel 1</li><li>Blogartikel 2</li><li>Blogartikel 3</li><li>Blogartikel 4</li></ul><ul class="link-list"><li>Blogartikel 5</li><li>Blogartikel 6</li><li>Blogartikel 7</li><li>Blogartikel 8</li></ul></div></div>
    </footer>
    <div class="site-copy">Copyright © 2017 Carolin Weber · info@carolinweber.de | Impressum • Datenschutz | Kontakt</div>
  </section>
  <div class="caption" style="left:60px;top:2010px">Entwurf - Über mich</div>

  <section class="page" style="left:673px;top:718px;height:1784px">
    <header class="site-header"><div class="site-name">CAROLIN WEBER</div><div class="site-slogan">Slogan - Subheadline</div></header>
    <nav class="site-nav"><span>Home</span><span class="active">Blog</span><span>Über mich</span><span>Kontakt</span></nav>
    <div class="site-body">
      <article class="main article">
        <h2 class="article-title">Wie bekomme ich sofort einen Termin beim Frauenarzt?</h2>
        <div class="post-meta"><span>03. Oktober 2017</span><span>2 Kommentare</span><span>Blogthema</span></div>
        <div class="post-image img-sleeping" role="img" aria-label="Foto: schlafendes Neugeborenes auf weißer Decke"></div>
        <p><span class="quote">"Tut mir leid, die nächsten drei Monate sind wir voll ausgebucht!"</span> - Worte, die jedem Patienten Ohrenschmerzen bereiten. Bei einem Facharzt sind sie bereits zum Standardrepertoire geworden, beim Gynäkologen. Wer hier auf einen schnellen Termin hofft, wartet oft vergebens. Nicht selten beträgt die Wartezeit bis zu vier Monate. Dem einen mögen vier Monate vielleicht wie nichts erscheinen, Frauen wie mir hingegen wie eine Ewigkeit.</p>
        <p>Wer sich nach neuem Leben sehnt, hat keine Zeit zu warten. So ist jeder verstrichene Tag ein verlorener Tag. Auch du willst dich nicht länger vertrösten lassen? Ich verrate dir meine Tipps, schneller an einen Termin beim Frauenarzt zu kommen.</p>
        <h3>1. Persönlich vorbeikommen</h3>
        <p>Jemanden durch den Telefonhörer abzuwimmeln ist keine große Kunst. Jemanden persönlich abzuwimmeln aber schon. Wer den weiten Weg zur Praxis bereits auf sich genommen hat, wird seltener wieder nach Hause geschickt. Ich zumindest bin davon immer verschont geblieben. Vor Ort musst du vielleicht mit langen Wartezeiten rechnen, erhöhst aber deine Chancen auf eine sofortige Behandlung. Vielleicht kannst du deinem Glück mit einem kleinen finanziellen Zuschuss in die Kaffeekasse der Sprechstundenhilfe auch ein wenig auf die Sprünge helfen. "Persönlich statt telefonisch" kann dich deinem Kinderwunsch also schon einmal einen entscheidenden Schritt näherbringen.</p>
        <h3>2. Zwischen 10 und 11 Uhr anrufen</h3>
        <p>Sich beim Gynäkologen noch am selben Tag einen Termin zu verschaffen, ist reine Utopie? Nicht unbedingt!</p>
        <p><strong>Mein persönliches Erfolgsgeheimnis: zwischen 10 und 11.</strong></p>
        <p>Das sind keine magischen Zahlen, sondern die Zeit, in der du zum Telefonhörer greifen solltest. Wenn es am selben Tag noch offene Termine gibt, dann weiß es die Praxis meist zwischen 10 und 11 Uhr morgens. Gerade bei schlechtem Wetter rückt dein Nachmittagstermin in greifbare Nähe. Wenn sich ein Patient nicht durch Wind und Wetter zur Behandlung quälen will, springst du natürlich gerne für ihn ein.</p>
        <h3>3. Anliegen verdeutlichen</h3>
        <p>Ob Unterleibsschmerzen, Blutungen oder Hormonschwankungen - mach dein Anliegen klar und deutlich. Denn wenn sich Deutlichkeit auszahlt, dann ist es bei der Terminvergabe beim Frauenarzt. Handelt es sich nämlich um einen besonders dringenden Fall, darfst du nicht einfach von der Sprechstundenhilfe abgewiesen werden. Du hast Anspruch auf eine fachkundige gynäkologische Betreuung.</p>
        <div class="info-box">
          <h5>Und dem nicht genug:</h5>
          <p>Notfälle haben immer Vorrang. Bei akuten Beschwerden müssen dir andere Patienten den Vortritt lassen. Am besten legst du dir bereits im Vorfeld eine kurze Beschreibung zurecht. Für mehr Sicherheit beim Telefonat empfehle ich dir außerdem einen Sprechzettel. Die kleine Hilfestellung wirkt wahre Wunder.</p>
          <svg width="52" height="84" viewBox="0 0 52 84" aria-hidden="true"><circle cx="30" cy="10" r="9" fill="#a9c2dc"/><path d="M18 28 H36 L28 68 Q27 74 33 72 L40 68 L38 78 Q26 86 17 80 Q12 76 14 68 L20 38 H14 Z" fill="#a9c2dc"/></svg>
        </div>
        <h3>4. Keine Nachricht hinterlassen</h3>
        <p>Eine Nachricht auf dem Anrufbeantworter ist keine Garantie für einen schnellen Termin. Im Gegenteil: Wenn keine Rückrufnummer hinterlassen oder zu undeutlich gesprochen wird, kann die Sprechstundenhilfe oft nichts für dich tun. Mir ist dieser Fehler selbst schon oft passiert. Anstatt der Sprechstundenhilfe habe ich mein Anliegen dankbar dem Anrufbeantworter mitgeteilt - leider jedes Mal ohne Rückruf.</p>
        <h3>5. Stoßzeiten meiden und flexibel sein</h3>
        <p>Wer um 8 Uhr morgens oder nach 17 Uhr um einen kurzfristigen Termin bittet, wird kaum Erfolg haben. Denn frühmorgens und nach Dienstschluss sind die Praxen am besten gefüllt. Dasselbe gilt für die Mittagspausen. Umso vielversprechender sind Termine außerhalb der klassischen Stoßzeiten wie vor- und nachmittags. Eine Regel steht aber über allem: Sei flexibel! Wenn dir die Sprechstundenhilfe einen Termin einräumt, dann nimm ihn wahr - ganz egal ob morgens um 8 oder abends um 19:30 Uhr. Wer weiß, wann sich die nächste Gelegenheit bietet?!</p>
        <h3>6. Jederzeit einsprungbereit sein</h3>
        <p>Wenn es mit dem Termin nicht sofort klappen will, ist noch nicht alles verloren. Mit kurzfristigen Absagen ist schließlich den ganzen Tag über zu rechnen. Wichtig ist nur, dass du deine Einsatzbereitschaft deutlich machst. Hinterlasse bei der Sprechstundenhilfe deine Nummer! Beim nächsten abgesagten Termin bist du ihr erster Ansprechpartner.</p>
        <h3>7. Hartnäckig bleiben</h3>
        <p>Hartnäckigkeit zahlt sich aus. Wer auf seiner Forderung beharrt, wird vielleicht nicht gerade zum Lieblingspatient der Frauenarztpraxis, kommt aber schneller zum Ziel. Nach zwei bis drei Anrufen ist mir der nächste Termin so gut wie sicher.</p>
        <h3>8. Terminservice nutzen</h3>
        <p>Trotz aller Bemühungen kann dich dein Gynäkologe nicht einschieben? Dann musst du dennoch nicht auf deine Untersuchung verzichten. Die Terminservices der Krankenkassen und Online-Vermittlungen wie arztfinder-online.de haben mich bis jetzt immer einem zuverlässigen Facharzt zugewiesen. Laut einer aktuellen Umfrage der BKV kannst du mit den flexiblen Diensten sogar bis zu 77 Tage einsparen, wertvolle Zeit, die du mit den wirklich wichtigen Dingen im Leben verbringen kannst.</p>
        <h3>9. Wartezeiten überbrücken</h3>
        <p>Ein kurzfristiger Termin hat seinen Preis, seinen zeitlichen Preis. Anstatt die lange Wartezeit aber mit Klatschmagazinen in der Frauenarztpraxis zu vergeuden, kannst du sie sinnvoll nutzen. Vereinbare mit der Sprechstundenhilfe eine Zeitspanne bis zur Behandlung, in der du ungestört Besorgungen machen kannst! Sei es Einkaufen, Amtserledigungen oder einfach ein Spaziergang - ich versuche immer das Beste aus meiner Wartezeit zu machen.</p>
        <div class="pager"><span>‹ Vorheriger Artikel</span><span>Nächster Artikel ›</span></div>
      </article>
      <aside class="sidebar" style="height:482px">
        <div class="avatar" role="img" aria-label="Porträtfoto der Bloggerin"></div>
        <div class="side-heading">Herzlich Willkommen</div>
        <div class="side-text">Lorem ipsum dolor sit amet, consetetur sadipscing elitr, sed diam nonumy eirmod tempor invidunt ut labore et dolore magna</div>
        <div class="side-heading">Social Media</div>
        <div class="social"><span></span><span></span><span></span></div>
        <div class="side-heading">Blog Themen</div>
        <ul class="topic-list"><li>Blog-Thema Nummer 1</li><li>Blog-Thema Nummer 2</li><li>Blog-Thema Nummer 3</li><li>Blog-Thema Nummer 4</li><li>Blog-Thema Nummer 5</li><li>Blog-Thema Nummer 6</li></ul>
      </aside>
    </div>
    <footer class="site-footer">
      <div class="footer-col footer-about"><h4>Über Carolin Weber</h4><div class="row"><div class="avatar" role="img" aria-label="Porträtfoto der Bloggerin"></div><p>Lorem ipsum dolor sit amet, consetetur sadipscing elitr, sed diam nonumy eirmod tempor invidunt ut labore et dolore magna aliquyam erat.</p></div></div>
      <div class="footer-col footer-follow"><h4>Folgen Sie mir</h4><div class="social"><span></span><span></span><span></span></div></div>
      <div class="footer-col footer-links"><h4>Wichtige Links</h4><ul><li>Kontakt</li><li>Impressum</li><li>Datenschutz</li></ul></div>
      <div class="footer-col"><h4>Meistgelesene Blogartikel</h4><div class="link-cols"><ul class="link-list"><li>Blogartikel 1</li><li>Blogartikel 2</li><li>Blogartikel 3</li><li>Blogartikel 4</li></ul><ul class="link-list"><li>Blogartikel 5</li><li>Blogartikel 6</li><li>Blogartikel 7</li><li>Blogartikel 8</li></ul></div></div>
    </footer>
    <div class="site-copy">Copyright © 2017 Carolin Weber · info@carolinweber.de | Impressum • Datenschutz | Kontakt</div>
  </section>
  <div class="caption" style="right:58px;top:2512px">Entwurf - Blog</div>
</div>
</div>
</body>
</html>
```